Personal Brand Business Card

I am looking for a design that I will use as my personal brand that conveys class (think 1920s gentlemen) and is timeless. I will be putting this on a pearl white, letter pressed, cotton business card.  I’m thinking maybe something with my initials on the front they will flip over for the rest of my information.  But don’t let that limit you.
The information I will have on the back of the business card will be my name, email, and phone number.
Some of the attributes that best describe me are: loyal, dependable, creative, risk taker, open minded, competitive, and empathetic.  I can adapt to my environment quickly and can get along with anyone.  I get excited by figuring out the way things work and finding solutions to problems.

Industry/Entity Type
Business

```html
<!DOCTYPE html>
<html lang="en">
<head>
<meta charset="utf-8">
<title>Grant Whitfield — Business Card</title>
<link rel="stylesheet" href="https://fonts.googleapis.com/css2?family=Oxygen:wght@300;400;700&display=swap">
<style>
  :root {
    --backdrop: #e6e6e4;
    --card: #fbfbf9;
    --ink: #1c1c1c;
    --ink-soft: #3a3a3a;
    --band-dark: #242424;
    --band-mid: #8a8a8a;
    --rule: #2a2a2a;
  }
  * { margin: 0; padding: 0; box-sizing: border-box; }
  html, body {
    width: 1200px; height: 873px; overflow: hidden;
    background: var(--backdrop);
    font-family: "Oxygen", sans-serif;
    color: var(--ink);
  }
  .sheet {
    position: relative; width: 1200px; height: 873px;
    display: flex; align-items: center; justify-content: center; gap: 60px;
  }
  .card {
    position: relative; width: 500px; height: 286px;
    background: var(--card);
    box-shadow: 0 2px 6px rgba(0,0,0,.18);
    overflow: hidden;
  }
  /* Back: contact side */
  .card__wave { position: absolute; inset: 0; width: 100%; height: 100%; }
  .card__name-block {
    position: absolute; top: 48px; right: 250px;
    text-align: right;
  }
  .card__name {
    font-size: 30px; font-weight: 400; line-height: 1.08; letter-spacing: .4px;
  }
  .card__role {
    font-size: 12px; font-weight: 300; color: var(--ink-soft); margin-top: 4px;
  }
  .card__divider {
    position: absolute; top: 36px; left: 262px;
    width: 1.5px; height: 160px; background: var(--rule);
  }
  .contact-list {
    position: absolute; top: 48px; left: 276px; right: 14px;
    list-style: none;
  }
  .contact-list__item {
    display: flex; align-items: center; gap: 8px;
    font-size: 14px; margin-bottom: 12px; white-space: nowrap;
  }
  .contact-list__icon { width: 22px; height: 22px; flex: none; }
  .contact-list__item--phone { font-size: 18px; letter-spacing: .5px; }

  /* Front: name mark */
  .card--front { display: flex; align-items: center; justify-content: center; gap: 18px; }
  .brand-square { width: 46px; height: 46px; background: var(--band-dark); }
  .brand-name { font-size: 40px; font-weight: 700; color: var(--band-dark); letter-spacing: .5px; }
</style>
</head>
<body>
<main class="sheet">
  <section class="card card--back" aria-label="Card back with contact details">
    <svg class="card__wave" viewBox="0 0 500 286" preserveAspectRatio="none" aria-hidden="true">
      <path d="M0 0 H120 C85 70 120 150 95 286 H0 Z" fill="var(--band-mid)"/>
      <path d="M0 0 H80 C50 70 85 160 55 286 H0 Z" fill="var(--band-dark)"/>
    </svg>
    <div class="card__name-block">
      <h1 class="card__name">Grant<br>Whitfield</h1>
      <p class="card__role">description</p>
    </div>
    <div class="card__divider"></div>
    <ul class="contact-list">
      <li class="contact-list__item">
        <svg class="contact-list__icon" viewBox="0 0 24 24" aria-hidden="true">
          <circle cx="12" cy="12" r="10.5" fill="none" stroke="var(--ink)" stroke-width="1.6"/>
          <path d="M9 6.5c-1.6 1-2 2.8-.6 5.2 1.5 2.6 3.4 4.5 5.6 5.4 1.2.5 2.2 0 2.9-1l-2-1.8-1.3 1c-1.4-.7-2.6-2-3.3-3.5l1.1-1.2z" fill="var(--ink)"/>
        </svg>
        <span>grantwhitfield@mail.com</span>
      </li>
      <li class="contact-list__item contact-list__item--phone">
        <svg class="contact-list__icon" viewBox="0 0 24 24" aria-hidden="true">
          <circle cx="12" cy="12" r="11" fill="var(--ink)"/>
          <rect x="6" y="8" width="12" height="8.5" fill="none" stroke="#fff" stroke-width="1.4"/>
          <path d="M6 8l6 5 6-5" fill="none" stroke="#fff" stroke-width="1.4"/>
        </svg>
        <span>555-014-2287</span>
      </li>
    </ul>
  </section>

  <section class="card card--front" aria-label="Card front with name mark">
    <span class="brand-square" aria-hidden="true"></span>
    <span class="brand-name">Grant Whitfield</span>
  </section>
</main>
</body>
</html>
```